Vor Mask business card

Create a new business card for Vor Mask. Black colour base front and back (the sides can be blue if that works) You can modify the blue colour to best suit the design. I am after a card that looks technical, modern and strong. one side with the Vor Mask and the other company details. The attached file has the details needed for the card. Crossway is the parent company name and needed but in a smaller size

Target Market(s)

Businesses (suppliers and customers)

Industry/Entity Type

Business

Contact Information for Business Card

Black colour base front and back

Font styles to use
Other font styles liked:
• attached

Requirements
Must have
• Logo's as attached

```html
<!DOCTYPE html>
<html lang="en">
<head>
<meta charset="utf-8">
<title>Vor Mask business card</title>
<link href="https://fonts.googleapis.com/css2?family=Open+Sans:wght@400;600;700&display=swap" rel="stylesheet">
<style>
  :root {
    --stage: #2a2a2a;
    --card: #15151a;
    --card-edge: #0c0c10;
    --blue: #2fa3d6;
    --blue-deep: #1d86b8;
    --grey: #a9a9ad;
    --white: #e8e8ea;
  }
  * { margin: 0; padding: 0; box-sizing: border-box; }
  html, body {
    width: 1200px; height: 900px; overflow: hidden;
    background: var(--stage);
    font-family: "Open Sans", Arial, sans-serif;
  }
  .card {
    position: absolute; left: 270px;
    width: 660px; height: 380px;
    background: var(--card);
    border: 1px solid var(--card-edge);
    overflow: hidden;
  }
  .card--front { top: 55px; }
  .card--back { top: 465px; }

  .brand { position: absolute; display: flex; align-items: center; gap: 12px; }
  .brand__mark { width: 14px; height: 14px; background: var(--blue); border-radius: 50%; }
  .brand__name {
    font-size: 42px; font-weight: 600; letter-spacing: 4px;
    color: var(--grey); text-transform: uppercase; line-height: 1;
  }
  .card--front .brand { left: 80px; top: 170px; }
  .card--back .brand { left: 80px; top: 100px; }

  .pattern-area {
    position: absolute; right: 0; top: 0; width: 320px; height: 290px;
    background: linear-gradient(135deg, rgba(47,163,214,0.05), rgba(47,163,214,0.22) 60%, rgba(47,163,214,0.04));
  }

  .contact { position: absolute; left: 400px; top: 58px; color: var(--white); }
  .contact__name { font-size: 22px; font-weight: 700; color: var(--blue); }
  .contact__role { font-size: 14px; margin: 2px 0 22px 10px; }
  .contact__line { display: flex; align-items: center; gap: 8px; font-size: 14px; margin-left: 22px; line-height: 22px; }
  .contact__icon { width: 14px; height: 14px; flex: none; }
  .contact__address { margin-top: 40px; align-items: flex-start; }
  .contact__address span { display: block; }

  .parent { position: absolute; left: 70px; top: 258px; color: var(--blue); }
  .parent__name { font-size: 28px; font-weight: 700; line-height: 1; }
  .parent__legal { font-size: 10px; margin-top: 6px; }

  .band { position: absolute; left: 0; bottom: 0; width: 660px; height: 110px; }
  .band__url {
    position: absolute; right: 36px; bottom: 62px;
    font-size: 15px; color: var(--white);
  }
</style>
</head>
<body>

<section class="card card--front">
  <div class="brand">
    <span class="brand__mark"></span>
    <span class="brand__name">Vor Mask</span>
  </div>
  <div class="pattern-area" role="img" aria-label="Blue technical line pattern decoration"></div>
</section>

<section class="card card--back">
  <div class="brand">
    <span class="brand__mark"></span>
    <span class="brand__name">Vor Mask</span>
  </div>

  <div class="contact">
    <div class="contact__name">Lena Ortwin</div>
    <div class="contact__role">Managing Director</div>
    <div class="contact__line">
      <svg class="contact__icon" viewBox="0 0 14 14"><circle cx="7" cy="7" r="6.5" fill="none" stroke="#2fa3d6"/><path d="M4.5 5c0 2.5 2 4.5 4.5 4.5l.6-1.2-1.4-.7-.6.6c-.8-.4-1.4-1-1.8-1.8l.6-.6-.7-1.4z" fill="#2fa3d6"/></svg>
      +61 400 555 018
    </div>
    <div class="contact__line">
      <svg class="contact__icon" viewBox="0 0 14 14"><circle cx="7" cy="7" r="6.5" fill="none" stroke="#2fa3d6"/><rect x="3.8" y="4.8" width="6.4" height="4.4" fill="#2fa3d6"/><path d="M3.8 4.8l3.2 2.4 3.2-2.4" fill="none" stroke="#15151a" stroke-width=".8"/></svg>
      lena@crosswayhold.com
    </div>
    <div class="contact__line contact__address">
      <svg class="contact__icon" viewBox="0 0 14 14" style="margin-top:4px"><circle cx="7" cy="7" r="6.5" fill="none" stroke="#2fa3d6"/><path d="M7 3.5a2.4 2.4 0 0 0-2.4 2.4C4.6 7.8 7 10.5 7 10.5s2.4-2.7 2.4-4.6A2.4 2.4 0 0 0 7 3.5z" fill="#2fa3d6"/><circle cx="7" cy="5.9" r=".9" fill="#15151a"/></svg>
      <div>
        <span>PO Box 120 Northgate</span>
        <span>S.A. 5999</span>
        <span>Australia</span>
      </div>
    </div>
  </div>

  <div class="parent">
    <div class="parent__name">Crossway</div>
    <div class="parent__legal">Crossway Holdings Pty Ltd</div>
  </div>

  <svg class="band" viewBox="0 0 660 110" preserveAspectRatio="none">
    <defs>
      <linearGradient id="bandFill" x1="0" y1="0" x2="0" y2="1">
        <stop offset="0" stop-color="#36acdd"/>
        <stop offset="1" stop-color="#1d86b8"/>
      </linearGradient>
    </defs>
    <path d="M0 62 L400 62 C430 62 430 22 460 22 L660 22 L660 110 L0 110 Z" fill="url(#bandFill)"/>
  </svg>
  <div class="band__url">www.crosswayhold.com</div>
</section>

</body>
</html>
```